Monthly Planner & To Do List on dry erase magnetic whiteboard

I'm after 2 x designs for magnetic whiteboards.
1. 17 x 13 inches is a monthly planner. Dates and month can be written in each month and then wiped off and re-written for the next month.
2. 6 x 4 inches - to do list however I don't want this to say To Do on it but will have lines to write on and possibly bullet points to check off.
I have attached below samples of other products (the ones I like the most are the first two - 9.19.52 and 9.20.34). I actually don't like the design of the others but just show them here as an example for layout purposes.
I want something that is modern, slick, simple yet stylish which is what my brand is representative of - smart, modern, organised. It will be printed onto a white board and I only want the print to be in black, no grey shading. I need a more modern font and don't like any of the swirly parts. Just clean and simple but slick.
I would like the size of the day squares to be as large as possible to fit writing in them and also for a section somewhere on the page for additional notes.

• Old style fonts, cartoon style or childish.

```html
<!DOCTYPE html>
<html lang="en">
<head>
<meta charset="utf-8">
<title>Monthly Planner – July 2018</title>
<link href="https://fonts.googleapis.com/css2?family=Federo&family=Lobster+Two:ital,wght@1,700&display=swap" rel="stylesheet">
<style>
  :root {
    --ink: #111111;
    --frame: #9a9a9a;
    --paper: #ffffff;
  }
  * { box-sizing: border-box; margin: 0; padding: 0; }
  html, body { width: 1200px; height: 918px; overflow: hidden; background: var(--paper); }
  .planner {
    position: relative; width: 1200px; height: 918px;
    border: 1px solid var(--frame); border-radius: 10px;
    color: var(--ink);
  }
  .month-grid {
    position: absolute; left: 28px; top: 18px; width: 927px; height: 882px;
    display: grid;
    grid-template-columns: repeat(7, 1fr);
    grid-template-rows: repeat(5, 1fr);
  }
  .day {
    position: relative;
    border: 1px solid var(--ink);
    border-radius: 10px;
  }
  .day-name {
    position: absolute; left: 12px; top: 10px;
    font-family: "Federo", sans-serif; font-size: 21px; letter-spacing: 0.5px;
  }
  .day-number {
    position: absolute; right: 14px; top: 10px;
    font-family: "Lobster Two", cursive; font-style: italic; font-weight: 700;
    font-size: 20px;
  }
  .event {
    position: absolute;
    font-family: "Lobster Two", cursive; font-style: italic; font-weight: 700;
    font-size: 10.5px; line-height: 1.3; white-space: nowrap;
  }
  .event + .event { }
  .event p + p { margin-top: 12px; }
  .span-arrow { position: absolute; left: 0; top: 0; pointer-events: none; }
  .month-label {
    position: absolute; left: 966px; top: 18px; width: 224px; height: 34px;
    border: 1px solid var(--ink); border-top: none; border-left: none;
    border-radius: 0 0 8px 0;
    border-bottom: 1px solid var(--ink);
    text-align: right; padding-right: 10px;
  }
  .month-label .month { font-family: "Lobster Two", cursive; font-style: italic; font-weight: 700; font-size: 18px; }
  .month-label .year { font-family: "Federo", sans-serif; font-size: 27px; margin-left: 14px; }
  .memo {
    position: absolute; left: 966px; top: 62px; width: 224px; height: 838px;
    border: 1px solid var(--ink); border-right: none; border-bottom: none;
    border-radius: 8px 0 0 0;
  }
  .memo-title {
    margin-top: 10px; text-align: center;
    font-family: "Federo", sans-serif; font-size: 24px; text-decoration: underline;
    text-underline-offset: 4px;
  }
  .memo-note {
    position: absolute; left: 43px; top: 357px;
    font-family: "Lobster Two", cursive; font-style: italic; font-weight: 700;
    font-size: 10.5px; white-space: nowrap;
  }
  .memo-arrow { position: absolute; left: 24px; top: 410px; }
</style>
</head>
<body>
<main class="planner">
  <section class="month-grid">
    <div class="day"><span class="day-name">SUN</span><span class="day-number">1</span></div>
    <div class="day"><span class="day-name">MON</span><span class="day-number">2</span>
      <div class="event" style="left:23px;top:60px"><p>Board Meeting<br>10 am</p></div></div>
    <div class="day"><span class="day-name">TUES</span><span class="day-number">3</span></div>
    <div class="day"><span class="day-name">WED</span><span class="day-number">4</span>
      <div class="event" style="left:11px;top:46px"><p>Web Seminar<br>2:15 pm</p><p>Softball Game 6:00 pm</p><p>Pick up wife 8:30 pm<br>@ &nbsp;Halvorsen's</p></div></div>
    <div class="day"><span class="day-name">THU</span><span class="day-number">5</span></div>
    <div class="day"><span class="day-name">FRI</span><span class="day-number">6</span></div>
    <div class="day"><span class="day-name">SAT</span><span class="day-number">7</span></div>

    <div class="day"><span class="day-number">8</span>
      <div class="event" style="left:27px;top:46px"><p>Board Flight 217 LKM<br>6:45 am</p></div></div>
    <div class="day"><span class="day-number">9</span>
      <div class="event" style="left:11px;top:38px"><p>Board FlighTrade Show</p></div></div>
    <div class="day"><span class="day-number">10</span></div>
    <div class="day"><span class="day-number">11</span></div>
    <div class="day"><span class="day-number">12</span></div>
    <div class="day"><span class="day-number">13</span>
      <div class="event" style="left:11px;top:63px"><p>Lakemont Airport<br>Flight 20<br>3 pm</p></div></div>
    <div class="day"><span class="day-number">14</span></div>

    <div class="day"><span class="day-number">15</span></div>
    <div class="day"><span class="day-number">16</span>
      <div class="event" style="left:33px;top:52px"><p>Opoker<br>Gmeeting with<br>CEO<br>9 am</p></div></div>
    <div class="day"><span class="day-number">17</span></div>
    <div class="day"><span class="day-number">18</span></div>
    <div class="day"><span class="day-number">19</span></div>
    <div class="day"><span class="day-number">20</span></div>
    <div class="day"><span class="day-number">21</span>
      <div class="event" style="left:28px;top:61px"><p>Opoker<br>Game at Rob's<br>7 PM</p></div></div>

    <div class="day"><span class="day-number">22</span></div>
    <div class="day"><span class="day-number">23</span></div>
    <div class="day"><span class="day-number">24</span></div>
    <div class="day"><span class="day-number">25</span></div>
    <div class="day"><span class="day-number">26</span></div>
    <div class="day"><span class="day-number">27</span></div>
    <div class="day"><span class="day-number">28</span></div>

    <div class="day"><span class="day-number">9</span></div>
    <div class="day"><span class="day-number">39</span></div>
    <div class="day"><span class="day-number">31</span></div>
    <div class="day"></div>
    <div class="day"></div>
    <div class="day"></div>
    <div class="day"></div>
  </section>

  <svg class="span-arrow" width="1200" height="918" aria-hidden="true">
    <line x1="206" y1="289" x2="625" y2="289" stroke="#111" stroke-width="3"/>
    <polygon points="646,289 618,279 624,289 618,299" fill="#111"/>
  </svg>

  <header class="month-label"><span class="month">July</span><span class="year">/ 2018</span></header>

  <aside class="memo">
    <h2 class="memo-title">Memo</h2>
    <p class="memo-note">Remember to cal xyz this week</p>
    <svg class="memo-arrow" width="110" height="20" aria-hidden="true">
      <line x1="16" y1="8" x2="104" y2="8" stroke="#111" stroke-width="3"/>
      <polygon points="0,8 24,0 19,8 24,16" fill="#111"/>
    </svg>
  </aside>
</main>
</body>
</html>
```